Postcard Mail Out - Wendell

We are a real estate company. We need a post card to mail out to potential clients to try and sale their land. We will attached a couple of post cards that we like but we do not want to copy them completely. We do need to put the Fair Dwelling Access and the Homevest logos with a disclosure saying not intended to solicit currently listed properties. The image below is what we had started working on. We would like to include something about farm land, timber, maybe a pond, something along those lines. The PDF Files attached are a flyer that was mailed out by another company that we do not want to copy completely. Attached also will be our company's Logo.

Requirements
Must have
• We do need to put the Fair Dwelling Access and the Homevest logos with a disclosure saying not intended to solicit currently listed properties.<br/><br/>At Sol Brantham Summit Realty, we are blessed to have one of the very best Rural Land Specialists available. Wendell has years of experience promoting and selling rural land properties. Wendell has earned the trust of many landowners, as he is so PASSIONATE in all regards to rural land, farms and ranches. He has made a wide range of landowners very happy throughout his years in Real Estate. Call him today and show him your property, and he will provide you with a free analysis and strategy to maximize the return on your property.
Nice to have
• A picture of Wendell has been added to use on the back of the post card with his phone and number. It would be nice to have a east Texas scenery picture behind him instead of an office.<br/><br/>Please include front and back of post card in your submission.
Should not have
• Should not have Marcus Vell's information on the postcard. That post card was just to show what we was wanting. The agent we want listed is Wendell Harbin and his phone number is (555)214-3098.

```html
<!DOCTYPE html>
<html lang="en">
<head>
<meta charset="utf-8">
<title>Postcard Mail Out – Wendell Harbin</title>
<link href="https://fonts.googleapis.com/css2?family=Libre+Baskerville:wght@400;700&family=Roboto+Condensed:wght@400;500;700&family=Roboto:wght@400;500&display=swap" rel="stylesheet">
<style>
  :root{
    --canvas:#e6e6e6;
    --charcoal:#3d3d3f;
    --charcoal-dark:#333335;
    --gold:#f2ae30;
    --wood-dark:#2b1e12;
    --wood-mid:#4a3420;
    --white:#ffffff;
    --ink:#2a2a2a;
    --muted:#555;
    --faint:#6a6a6a;
  }
  *{box-sizing:border-box;margin:0;padding:0}
  html,body{width:1039px;height:1200px;overflow:hidden}
  body{background:var(--canvas);position:relative;font-family:"Roboto Condensed",sans-serif;color:var(--ink)}
  .card{position:absolute;left:170px;width:700px;height:450px;background:var(--white);overflow:hidden;box-shadow:0 4px 10px rgba(0,0,0,.25)}
  .card-front{top:110px}
  .card-back{top:625px}

  /* FRONT */
  .front-header{position:absolute;left:0;top:0;width:700px;height:98px;
    background:repeating-linear-gradient(90deg,var(--wood-dark) 0 38px,var(--wood-mid) 38px 40px,#3a2817 40px 80px,var(--wood-dark) 80px 82px);
    display:flex;align-items:center;justify-content:center}
  .front-title{font-family:"Libre Baskerville",serif;font-weight:700;color:var(--white);font-size:66px;letter-spacing:1px;text-shadow:2px 2px 4px rgba(0,0,0,.6)}
  .photo{position:absolute}
  .photo-homestead{left:0;top:104px;width:275px;height:250px;background:linear-gradient(170deg,#cfe3f2 0%,#9bbf6a 30%,#5e9a3a 70%,#4a7d2c 100%)}
  .photo-pasture{left:278px;top:104px;width:185px;height:123px;background:linear-gradient(180deg,#7d8a78 0%,#6f9b47 45%,#4c7d2e 100%)}
  .photo-river{left:278px;top:230px;width:185px;height:124px;background:linear-gradient(180deg,#a9c6e6 0%,#7b8a6a 40%,#8a8f62 70%,#6b7a44 100%)}
  .photo-pines{left:466px;top:104px;width:234px;height:250px;background:linear-gradient(180deg,#6f8a5a 0%,#3f5a2e 50%,#5c6b35 100%)}
  .front-footer{position:absolute;left:0;top:364px;width:700px;height:86px;background:var(--charcoal)}
  .front-tag{position:absolute;left:0;top:29px;height:36px;width:394px;background:var(--gold);
    clip-path:polygon(0 0,383px 0,394px 100%,0 100%);
    color:var(--white);font-weight:700;font-size:20px;line-height:36px;padding-left:18px;letter-spacing:.3px}
  .front-brand{position:absolute;right:26px;top:38px;font-family:"Libre Baskerville",serif;font-size:15px;color:#6c6c6e}

  /* BACK */
  .back-hero{position:absolute;left:0;top:0;width:700px;height:200px;
    background:linear-gradient(90deg,rgba(255,255,255,.95) 0%,rgba(255,255,255,.85) 50%,rgba(255,255,255,0) 68%),linear-gradient(180deg,#e9f1f7 0%,#d9e2e8 55%,#d8c79a 75%,#c7b07a 100%)}
  .back-intro{position:absolute;left:18px;top:20px;width:356px}
  .back-heading{font-weight:700;font-size:16px;color:#1d1d1d;margin-bottom:9px}
  .back-copy{font-family:"Roboto",sans-serif;font-size:11px;line-height:14.6px;color:var(--ink);letter-spacing:-.2px}
  .back-copy + .back-copy{margin-top:15px}
  .agent-photo{position:absolute;left:550px;top:6px;width:150px;height:194px;background:linear-gradient(180deg,#c9cfd4 0%,#2a2a30 45%,#1c1c22 100%);border-radius:60px 60px 0 0}
  .brand-mark{position:absolute;left:398px;top:48px;display:flex;align-items:center;gap:6px}
  .brand-mark .dot{width:12px;height:12px;background:var(--ink)}
  .brand-mark span{font-family:"Libre Baskerville",serif;font-weight:700;font-size:12px;color:var(--ink);line-height:14px}
  .agent-name{position:absolute;left:390px;top:103px;font-family:"Libre Baskerville",serif;font-weight:700;font-size:17px;color:#1e1e1e}
  .agent-contact{position:absolute;left:386px;width:170px;height:18px;background:rgba(60,60,50,.85);color:var(--white);font-family:"Roboto",sans-serif;font-weight:500;font-size:10px;line-height:18px;padding-left:20px}
  .agent-contact svg{position:absolute;left:5px;top:4px}
  .contact-phone{top:126px}
  .contact-web{top:147px}
  .badges{position:absolute;left:388px;top:174px;display:flex;align-items:center;gap:4px}
  .badge{width:14px;height:14px;background:#222}
  .badges p{font-size:5px;font-weight:700;line-height:5.5px;width:68px;text-transform:uppercase}

  .back-panel{position:absolute;left:0;top:200px;width:372px;height:212px;background:var(--charcoal)}
  .panel-heading{font-weight:700;font-size:14px;color:var(--gold);letter-spacing:-.2px}
  .tools-heading{position:absolute;left:18px;top:17px}
  .tools{position:absolute;left:18px;top:42px;display:grid;grid-template-columns:203px 150px;row-gap:6px}
  .tool{display:flex;align-items:center;gap:6px;color:var(--white);font-family:"Roboto",sans-serif;font-size:10.5px}
  .tool-icon{width:17px;height:17px;border:1.5px solid #cfcfcf;border-radius:3px;display:flex;align-items:center;justify-content:center}
  .tool-icon i{width:7px;height:7px;background:var(--gold);border-radius:50%}
  .promises-heading{position:absolute;left:18px;top:110px}
  .promises{position:absolute;left:18px;top:132px;list-style:none}
  .promises li{color:var(--white);font-family:"Roboto",sans-serif;font-size:10px;line-height:17px;padding-left:13px;position:relative}
  .promises li::before{content:"";position:absolute;left:0;top:5px;width:7px;height:7px;border-radius:50%;background:var(--gold)}
  .back-bar{position:absolute;left:0;top:412px;width:382px;height:38px;background:var(--gold);clip-path:polygon(0 0,372px 0,372px 0,382px 10px,382px 100%,0 100%);display:flex;align-items:center;gap:26px;padding-left:18px;color:var(--white);font-weight:500;font-size:19px}
  .back-bar span{display:flex;align-items:center;gap:8px}

  .return-address{position:absolute;left:394px;top:227px;font-family:"Roboto",sans-serif;color:var(--faint);font-size:10px;line-height:13px}
  .return-address strong{display:block;font-weight:400;color:#222;font-size:11.5px;margin-bottom:5px}
  .postage{position:absolute;left:625px;top:218px;width:62px;height:59px;border:1px solid #888;font-family:Arial,sans-serif;font-size:8px;line-height:10px;color:#555;text-align:center;padding-top:3px}
  .postage b{color:#333}
  .mail-block{position:absolute;left:519px;top:305px;width:169px;height:67px;border:1px solid #888;font-family:Arial,sans-serif;color:#555}
  .mail-block .route{position:absolute;right:12px;top:8px;font-size:7px}
  .mail-block .recipient{position:absolute;left:12px;top:34px;font-size:9px;line-height:11px}
</style>
</head>
<body>

<section class="card card-front" aria-label="Postcard front">
  <header class="front-header"><h1 class="front-title">LAND FOR SALE?</h1></header>
  <div class="photo photo-homestead" role="img" aria-label="Aerial photo of a white farmhouse on green rolling pasture"></div>
  <div class="photo photo-pasture" role="img" aria-label="Green hillside pasture with a tractor"></div>
  <div class="photo photo-river" role="img" aria-label="River running through a valley below mountains"></div>
  <div class="photo photo-pines" role="img" aria-label="Stand of tall pine timber"></div>
  <footer class="front-footer">
    <div class="front-tag">SPECIALIZING IN RURAL LAND SALES</div>
    <div class="front-brand">Sol Brantham Summit Realty</div>
  </footer>
</section>

<section class="card card-back" aria-label="Postcard back">
  <div class="back-hero" role="img" aria-label="Open east Texas grassland under a pale sky with a windmill"></div>
  <div class="back-intro">
    <h2 class="back-heading">THINKING ABOUT SELLING YOUR LAND?</h2>
    <p class="back-copy">My name is Wendell Harbin. I am an experienced Rural Land Specialist. I have been trusted by many land owners to market, advertise and sell their properties. I'm very passionate about rural land and have been very successful in selling a lot of properties; therefore, making many landowners very happy.</p>
    <p class="back-copy">Call me today and show me your property and I'll then provide you with a free analysis and strategy for selling your land to maximize your return on your investment.</p>
  </div>
  <div class="agent-photo" role="img" aria-label="Portrait of agent Wendell Harbin on the phone"></div>
  <div class="brand-mark"><i class="dot"></i><span>Sol Brantham<br>Summit Realty</span></div>
  <div class="agent-name">Wendell Harbin</div>
  <div class="agent-contact contact-phone">
    <svg width="10" height="10" viewBox="0 0 10 10"><path d="M2 1l2 2-1 1.2c.6 1.2 1.6 2.2 2.8 2.8L7 6l2 2-1.3 1.3C4.5 9 1 5.5.7 2.3z" fill="#f2ae30"/></svg>(555)214-3098</div>
  <div class="agent-contact contact-web">
    <svg width="10" height="10" viewBox="0 0 10 10"><circle cx="5" cy="5" r="4" fill="none" stroke="#f2ae30" stroke-width="1.4"/><path d="M1 5h8M5 1v8" stroke="#f2ae30" stroke-width="1"/></svg>www.1summitlandprop.com</div>
  <div class="badges" aria-label="Homevest and Fair Dwelling Access">
    <i class="badge"></i><i class="badge"></i>
    <p>Not intended to solicit currently listed properties</p>
  </div>

  <div class="back-panel">
    <h3 class="panel-heading tools-heading">MARKETING TOOLS:</h3>
    <div class="tools">
      <div class="tool"><span class="tool-icon"><i></i></span>Internet Marketing</div>
      <div class="tool"><span class="tool-icon"><i></i></span>Email Newsletters</div>
      <div class="tool"><span class="tool-icon"><i></i></span>Advertising on #1 Land Website</div>
      <div class="tool"><span class="tool-icon"><i></i></span>Social Media advertising</div>
    </div>
    <h3 class="panel-heading promises-heading">AT RURAL LAND PROPERTIES WE:</h3>
    <ul class="promises">
      <li>We Are Passionate about Rural Land</li>
      <li>We Identify Best Marketable Value of your Land</li>
      <li>We Target Likely Buyers Nationwide</li>
      <li>We Are Known for Honesty &amp; Integrity</li>
    </ul>
  </div>
  <div class="back-bar">
    <span><svg width="16" height="16" viewBox="0 0 10 10"><path d="M2 1l2 2-1 1.2c.6 1.2 1.6 2.2 2.8 2.8L7 6l2 2-1.3 1.3C4.5 9 1 5.5.7 2.3z" fill="#fff"/></svg>(555)214-3098</span>
    <span><svg width="16" height="16" viewBox="0 0 10 10"><circle cx="5" cy="5" r="4" fill="none" stroke="#fff" stroke-width="1.4"/><path d="M1 5h8M5 1v8" stroke="#fff" stroke-width="1"/></svg>1summitlandprop.com</span>
  </div>

  <address class="return-address"><strong>Sol Brantham Summit Realty</strong>48 Ridge Rd&nbsp; Pinecrest, TX 75000<br>Office: 555-318-4402</address>
  <div class="postage">PRSRT STD<br>ECRWSS<br>U.S. Postage<br><b>PAID</b><br>EDDM RETAIL</div>
  <div class="mail-block">
    <span class="route">*******************ECRWSS****</span>
    <span class="recipient">Local<br>Postal Customer</span>
  </div>
</section>

</body>
</html>
```